Legal Information Website

We need a website that will serve as a source of information for people visiting, living, and working in the United Arab Emirates, where they can go and read about legal issues, laws, crimes, and most important find legal advice and find lawyers. The following are the pages of the website:

Find a Lawyer (Home Page)
This main feature of this page should be "Find a Lawyer"
Find a Lawyer should include the searching option by practice, by lawyer’s name, by law firm name or by location.

Ask a lawyer
This function allows the user to ask a lawyer a legal question and get an answer directly from a lawyer.

Research a legal matter
This function allows the user to do research on a certain legal topic. He/she can select from different legal topics.

Contact Us:
This page should include our contact details for the visitors in case they need any assistance. Contact us by Phone, Email, or Chat.

Once the design is approved, we will provide the rest of the website text.

Target Market(s)

General Public who seek legal advice

Industry/Entity Type

Law Firm

Font styles to use
Serif
Sans Serif

Requirements
Must have
• A tool to search for lawyer's, and then display the lawyer's picture and profile and credentials.

```html
<!DOCTYPE html>
<html lang="en">
<head>
<meta charset="utf-8">
<title>LexHarbor – Find the Right Lawyer</title>
<link href="https://fonts.googleapis.com/css2?family=Signika:wght@400;600;700&family=Open+Sans:wght@400;600;700&family=Mulish:wght@400;500&display=swap" rel="stylesheet">
<style>
:root{
  --ink:#222;
  --muted:#777;
  --blue:#1d63ad;
  --blue-bright:#2f80c3;
  --yellow:#fcc20f;
  --yellow-dark:#e2a400;
  --orange:#f07b16;
  --topbar:#1b1e21;
  --footer:#202223;
  --footer-line:#333;
  --bottombar:#1566b9;
  --page:#f6f6f6;
  --line:#e2e2e2;
}
*{box-sizing:border-box;margin:0;padding:0}
html,body{width:733px;height:1200px;overflow:hidden;background:#fff}
body{font-family:"Open Sans",Arial,sans-serif;color:var(--ink)}
ul{list-style:none}
a{color:inherit;text-decoration:none}
.page{position:relative;width:733px;height:1200px;overflow:hidden;background:var(--page)}
.abs{position:absolute}

/* top bar */
.topbar{left:0;top:0;width:733px;height:21px;background:var(--topbar);color:#bbb;font-size:6.6px}
.topbar .links{position:absolute;left:82px;top:6px}
.topbar .help{position:absolute;right:81px;top:5px;color:#fff;font-weight:600;font-size:7px}
.topbar .help b{color:var(--yellow)}

/* nav */
.navbar{left:0;top:21px;width:733px;height:33px;background:linear-gradient(#efefef,#dedede);border-bottom:1px solid #cfcfcf}
.brand{position:absolute;left:82px;top:8px;font-family:"Signika",sans-serif;font-weight:700;font-size:17px;color:var(--blue);letter-spacing:.2px}
.menu{position:absolute;left:376px;top:0;display:flex;height:33px}
.menu li{padding:0 14px;line-height:33px;font-family:"Signika",sans-serif;font-weight:600;font-size:7.6px;border-left:1px solid #cfcfcf}
.menu li:last-child{border-right:1px solid #cfcfcf}
.menu li.active{color:var(--blue)}

/* hero */
.hero{left:0;top:54px;width:733px;height:259px;background:
  radial-gradient(ellipse at 70% 60%,rgba(230,150,50,.55),transparent 55%),
  radial-gradient(ellipse at 20% 80%,rgba(200,120,40,.45),transparent 50%),
  linear-gradient(#3d4a55,#1e2830 55%,#2a261e)}
.hero-text{position:absolute;left:0;top:78px;width:733px;text-align:center;color:#fff}
.hero h1{font-family:"Signika",sans-serif;font-weight:600;font-size:21px;line-height:23px;letter-spacing:.4px}
.hero p{font-size:10.4px;line-height:14px;margin-top:6px}
.btn{display:inline-block;background:linear-gradient(var(--yellow),var(--yellow-dark));color:#222;font-family:"Signika",sans-serif;font-weight:600;text-transform:uppercase;border-radius:2px}
.hero .btn{width:132px;height:23px;line-height:23px;font-size:10px;margin-top:12px}
.dots{position:absolute;left:352px;top:220px;display:flex;gap:4px}
.dots i{width:7px;height:7px;border-radius:50%;background:#ccc}
.dots i.on{background:var(--yellow)}

/* sidebar */
.sidebar{left:81px;top:313px;width:161px;height:700px;background:#fff;border-right:1px solid var(--line)}
.search{background:var(--blue-bright);height:172px;padding:15px 14px 0;color:#fff}
.search h2{font-family:"Signika",sans-serif;font-weight:600;font-size:11px;line-height:12px}
.search p{font-size:5.8px;line-height:7.5px;margin-top:3px}
.field{height:18px;background:#fff;border-radius:2px;margin-top:3px;color:#333;font-size:6.2px;line-height:18px;padding-left:7px;position:relative}
.field:first-of-type{margin-top:7px}
.field .spin{position:absolute;right:0;top:0;width:10px;height:18px;background:#2a2a2a;border-radius:0 2px 2px 0}
.search .btn{display:block;width:133px;height:22px;line-height:22px;text-align:center;font-size:9.5px;margin-top:6px}
.side-block{padding:0 14px}
.side-title{font-family:"Signika",sans-serif;font-weight:600;font-size:10.5px;color:var(--blue);text-transform:uppercase}
.news{margin-top:10px}
.news li{border-bottom:1px solid var(--line);padding:8px 0 6px}
.news h3{font-family:"Mulish",sans-serif;font-weight:500;font-size:7.6px;line-height:10px;color:#222}
.news .src{font-size:5.2px;color:#555;margin-top:3px}
.news .src em{font-style:normal;color:var(--orange)}
.small-btn{display:inline-block;height:14px;line-height:14px;padding:0 8px;font-size:5.8px}
.rights-img{width:133px;height:69px;margin-top:14px;background:linear-gradient(135deg,#e6c98a,#a8763a 60%,#5a3a1c)}
.rights p{font-size:5.8px;line-height:7.5px;color:#333;margin-top:6px}
.ticks{margin-top:4px}
.ticks li{font-size:5.8px;font-weight:700;border-bottom:1px solid var(--line);padding:4px 0 4px 8px;position:relative}
.ticks li:before,.practice li:before{content:"";position:absolute;left:0;top:7px;width:3px;height:3px;border-radius:50%;background:#bbb}

/* main */
.main{left:272px;top:313px;width:381px}
.welcome h1{font-family:"Signika",sans-serif;font-weight:600;font-size:17.5px;color:var(--blue);margin-top:23px}
.lead{font-family:"Mulish",sans-serif;font-size:9.6px;line-height:12px;margin-top:6px;color:#222}
.body{font-size:7.2px;line-height:9.4px;color:#777;margin-top:9px}
.section-head{display:flex;justify-content:space-between;align-items:center;border-bottom:1px solid var(--line);padding-bottom:8px}
.section-head h2{font-family:"Signika",sans-serif;font-weight:600;font-size:10.5px;color:var(--blue);text-transform:uppercase}
.section-head h2 b{color:#222;font-weight:600}
.practice-wrap{position:absolute;top:189px;width:381px}
.practice{display:grid;grid-template-columns:95px 95px 95px;column-gap:48px;margin-top:6px}
.practice li{position:relative;font-size:6.3px;font-weight:700;color:#333;padding:3px 0 3px 10px;border-bottom:1px solid #ececec;line-height:7.3px}
.articles-wrap{position:absolute;top:349px;width:381px}
.articles-wrap .section-head{border:none;padding:0}
.article{display:flex;gap:10px;border-bottom:1px solid var(--line);padding:12px 0 14px}
.article:first-of-type{padding-top:15px}
.thumb{width:69px;height:64px;flex:none}
.t1{background:linear-gradient(135deg,#eef1f6,#9aa8c0 50%,#2b3a5a)}
.t2{background:linear-gradient(#8ab8dc,#d8cfae 60%,#b49a6e)}
.t3{background:linear-gradient(#cfd7df,#8a5e4c 45%,#5c4a42)}
.article h3{font-family:"Mulish",sans-serif;font-weight:400;font-size:10.4px;color:#222;margin-top:-1px}
.article p{font-size:5.9px;line-height:7.5px;color:#555;margin-top:6px}
.meta{font-size:5.2px;color:#333;margin-top:4px}
.meta em{font-style:normal;color:var(--orange)}
.articles-wrap .small-btn{margin-top:10px}

/* footer */
.footer{left:0;top:1013px;width:733px;height:155px;background:var(--footer);color:#aaa}
.fcol{position:absolute;top:27px}
.fcol h4{font-family:"Signika",sans-serif;font-weight:600;font-size:8.6px;color:#fff;text-transform:uppercase;margin-bottom:6px}
.fcol li{font-size:6.2px;line-height:11.5px;border-bottom:1px solid var(--footer-line);width:82px;padding-left:10px;position:relative}
.fcol li:before{content:"";position:absolute;left:1px;top:5px;width:2px;height:2px;background:#666}
.contact p{display:flex;gap:9px;font-size:7.6px;margin-bottom:8px;align-items:flex-start;line-height:10px}
.contact .phone{color:#fff;font-weight:700;font-size:9px}
.contact svg{flex:none;margin-top:1px}
.bottombar{left:0;top:1168px;width:733px;height:32px;background:var(--bottombar);color:#0d2d55;font-size:6px}
.follow{position:absolute;left:81px;top:6px;display:flex;align-items:center;gap:3px}
.follow i{width:5px;height:5px;border-radius:50%;background:#0d2d55}
.copy{position:absolute;left:81px;top:18px}
.foot-brand{position:absolute;right:80px;top:6px;font-family:"Signika",sans-serif;font-weight:700;font-size:17px;color:#0f3a6c}
</style>
</head>
<body>
<div class="page">

  <div class="abs topbar">
    <div class="links">Get Listed Today &nbsp;:&nbsp; Testimonials &nbsp;:&nbsp; International &nbsp;:&nbsp; Resources &nbsp;:&nbsp; Blog</div>
    <div class="help">Get Help Now : &nbsp;<b>800 555 0142</b></div>
  </div>

  <header class="abs navbar">
    <div class="brand">LEXHARBOR</div>
    <ul class="menu">
      <li class="active">HOME</li><li>RIGHTS</li><li>NEWS</li><li>ARTICLES</li><li>CONTACT US</li>
    </ul>
  </header>

  <section class="abs hero" role="img" aria-label="Night aerial photograph of a city skyline with glowing highways">
    <div class="hero-text">
      <h1>COUNSELPOINT HELPS<br>YOU FIND THE RIGHT LAWYER</h1>
      <p>Fast, Free and Confidential. Get started today and choose from<br>qualified professionals near you.</p>
      <a class="btn">Get Started</a>
    </div>
    <div class="dots"><i></i><i class="on"></i><i></i></div>
  </section>

  <aside class="abs sidebar">
    <div class="search">
      <h2>SEARCH FOR TOP-RATED<br>LAWYERS NEAR YOU</h2>
      <p>This is a sample version of Lorem Ipsum.<br>Proin gravida nibh vel velit auctor aliquet.</p>
      <div class="field">Lawyer's Name</div>
      <div class="field">Practice Area<span class="spin"></span></div>
      <div class="field">Location<span class="spin"></span></div>
      <a class="btn">Find Lawyer</a>
    </div>

    <div class="side-block" style="margin-top:22px">
      <h2 class="side-title">Recent News</h2>
      <ul class="news">
        <li><h3>Verdict in Florida 'loud music' death again raises self- defense issue</h3><div class="src">The Daily Ledger <em>2 days ago</em></div></li>
        <li><h3>Local Defendant on Channel 9: I'm homeless, suffering from PTSD</h3><div class="src">The Coastal Courier <em>3 days ago</em></div></li>
        <li><h3>Team Captain apologizes to Three Teammates</h3><div class="src">Wire Desk <em>2 days ago</em></div></li>
        <li style="border:none"><h3>Former congressman denies pornography charge in Zimbabwe</h3><div class="src">The Daily Ledger <em>2 days ago</em></div></li>
      </ul>
      <a class="btn small-btn" style="margin-top:4px">See All</a>
    </div>

    <div class="side-block rights" style="margin-top:22px">
      <h2 class="side-title">Know Your Rights?</h2>
      <div class="rights-img" role="img" aria-label="Photograph of a judge's gavel resting on a constitution document"></div>
      <p>This is a sample version of Lorem Ipsum. Proin gravida nibh vel velit auctor aliquet. Aenean sollicitudin, lorem quis bibendum auctor, nisi elit consequat ipsum.</p>
      <ul class="ticks">
        <li>UNIVERSAL AND INALIENABLE</li>
        <li>INTERDEPENDENT AND INDIVISIBLE</li>
        <li>EQUAL AND NON-DISCRIMINATORY</li>
        <li style="border:none">BOTH RIGHTS AND OBLIGATIONS</li>
      </ul>
      <a class="btn small-btn" style="margin-top:4px">Know Your Rights</a>
    </div>
  </aside>

  <main class="abs main">
    <section class="welcome">
      <h1>WELCOME TO OUR WEBSITE</h1>
      <p class="lead">This is a sample version of Lorem Ipsum. Proin gravida nibh vel velit auctor aliquet. Aenean sollicitudin, lorem quis bibendum auctor, nisi elit consequat ipsum, nec sagittis sem nibh id elit.</p>
      <p class="body">Duis sed odio sit amet nibh vulputate cursus a sit amet mauris. Morbi accumsan ipsum velit. Nam nec tellus a odio tincidunt auctor a ornare odio. Sed non mauris vitae erat consequat auctor eu in elit. Class aptent taciti sociosqu ad litora torquent per conubia nostra, per inceptos himenaeos. Mauris in erat justo. Nullam ac urna eu felis dapibus condimentum sit amet a augue. Sed non neque elit. Sed ut imperdiet nisi. Proin condimentum fermentum nunc. Etiam pharetra, erat sed fermentum feugiat, velit mauris egestas quam, ut aliquam massa nisl quis neque. Suspendisse in orci enim.</p>
    </section>

    <section class="practice-wrap">
      <div class="section-head">
        <h2>View Lawyers <b>by</b> Practice Area</h2>
        <a class="btn small-btn">See All Practice Area</a>
      </div>
      <ul class="practice">
        <li>BANKRUPTCY / DEBT</li><li>ESTATE PLANNING</li><li>PERSONAL INJURY</li>
        <li>BUSINESS</li><li>FAMILY</li><li>REAL ESTATE</li>
        <li>CIVIL RIGHTS</li><li>FORECLOSURE</li><li>SPEEDING / TRAFFIC</li>
        <li>CRIMINAL DEFENSE</li><li>FRAUD</li><li>TICKET</li>
        <li>DIVORCE / SEPARATION</li><li>IMMIGRATION</li><li>BUSINESS LAW</li>
        <li>DUI / DWI</li><li>LANDLORD / TENANT</li><li>TAX</li>
        <li style="border:none">EMPLOYMENT / LABOR</li><li style="border:none">LAWSUITS / DISPUTES</li><li style="border:none">GOVERNMENT</li>
      </ul>
    </section>

    <section class="articles-wrap">
      <div class="section-head"><h2><b>Top 10</b> Articles</h2></div>
      <article class="article">
        <div class="thumb t1" role="img" aria-label="Photograph of printed insurance documents"></div>
        <div><h3>Title Insurance Legal Disputes</h3>
          <p>Title insurance legal disputes can sometimes arise when title to a plot of land or real estate property is transferred from one person to another. Title insurance is often a major part of the transaction, since it provides protection for the major parties involved, such as the buyer, the seller, and loan or mortgage companies.</p>
          <div class="meta">Published by : <em>Mara Ellison</em> &nbsp;|&nbsp; February 12, 2014 &nbsp;|&nbsp; Government and Real Estate</div></div>
      </article>
      <article class="article">
        <div class="thumb t2" role="img" aria-label="Photograph of a sunny public beach"></div>
        <div><h3>California Senator Seeks to Reopen a Beach Blocked...</h3>
          <p>Title insurance legal disputes can sometimes arise when title to a plot of land or real estate property is transferred from one person to another. Title insurance is often a major part of the transaction, since it provides protection for the major parties involved, such as the buyer, the seller, and loan or mortgage companies.</p>
          <div class="meta">Published by : <em>Mara Ellison</em> &nbsp;|&nbsp; February 12, 2014 &nbsp;|&nbsp; Government and Real Estate</div></div>
      </article>
      <article class="article" style="border:none">
        <div class="thumb t3" role="img" aria-label="Photograph of a brick apartment building"></div>
        <div><h3>California Senator Seeks to Reopen a Beach Blocked...</h3>
          <p>Title insurance legal disputes can sometimes arise when title to a plot of land or real estate property is transferred from one person to another. Title insurance is often a major part of the transaction, since it provides protection for the major parties involved, such as the buyer, the seller, and loan or mortgage companies.</p>
          <div class="meta">Published by : <em>Mara Ellison</em> &nbsp;|&nbsp; February 12, 2014 &nbsp;|&nbsp; Government and Real Estate</div></div>
      </article>
      <a class="btn small-btn" style="margin-top:0">See All Articles</a>
    </section>
  </main>

  <footer class="abs footer">
    <div class="fcol" style="left:80px"><h4>Company Info</h4>
      <ul><li>About Us</li><li>Support</li><li>Press Room</li><li>Partner With Us</li><li>Jobs</li><li>Blog</li><li>Contact Us</li></ul></div>
    <div class="fcol" style="left:214px"><h4>Quick Links</h4>
      <ul><li>Legal Topics</li><li>State Laws</li><li>Bookshelf</li><li>Blogs</li><li>LawDesk RSS Feeds</li><li>Sitemap</li><li>LawWiki</li></ul></div>
    <div class="fcol" style="left:344px"><h4>Popular CounselPoint Pages</h4>
      <ul><li>Alabama Lawyers</li><li>Arizona Lawyers</li><li>Arkansas Lawyers</li><li>California Lawyers</li><li>Florida Lawyers</li><li>Georgia Lawyers</li><li>Illinois Lawyers</li></ul></div>
    <div class="fcol contact" style="left:540px"><h4 style="margin-bottom:11px">Contact Us</h4>
      <p><svg width="7" height="10" viewBox="0 0 7 10"><path d="M3.5 0A3.5 3.5 0 0 0 0 3.5C0 6 3.5 10 3.5 10S7 6 7 3.5A3.5 3.5 0 0 0 3.5 0zm0 5a1.4 1.4 0 1 1 0-2.8 1.4 1.4 0 0 1 0 2.8z" fill="#999"/></svg><span>418 Meridian Court<br>Harlow, OR 97401</span></p>
      <p><svg width="7" height="10" viewBox="0 0 7 10"><rect x="0.5" y="0.5" width="6" height="9" rx="1" fill="none" stroke="#fff"/><rect x="2.5" y="7.5" width="2" height="1" fill="#fff"/></svg><span class="phone">555-214-7730</span></p>
      <p><svg width="8" height="6" viewBox="0 0 8 6"><rect width="8" height="6" fill="#999"/><path d="M0 0l4 3.5L8 0" fill="none" stroke="#202223" stroke-width=".8"/></svg><span style="font-size:6.6px">help@lexharbor.example</span></p>
    </div>
  </footer>

  <div class="abs bottombar">
    <div class="follow">Follow us on &nbsp;<i></i><i></i><i></i><i></i></div>
    <div class="copy">©2014 LexHarbor. All Rights Reserved</div>
    <div class="foot-brand">LEXHARBOR</div>
  </div>

</div>
</body>
</html>
```